Admin Backend Redesign

We need a redesign for our backend which supoosed to make the backoffice look more modern!

I will add screenshots of the backoffice so you know what data will be shown in the Admin.

Have in mind that the users of this backend are Doctors. We need a clinical look, modern and sharp. The backoffice is responsive, have that in mind. We need the backoffice to look as professional as possible.

The theme used for the website is: http://velmora.quillstack-sample.com/

ON the main page of the backoffice, under every widget i need some space to write an explanation what the widget is about.

The color code used in our logo and website is #57aad4 combined with white.

We are open for ideas!
Updates

Project Deadline Extended
Reason: Designs are ok, but nothing innovative. Please use more modern designs!

Project Deadline Extended
Reason: Havent recieved a perfect design yet. Please read instructions carefully! Thank you

Project Deadline Extended
Reason: Hey everybody, sorry for the delay. We will decide in 3 days. If anyone wants to add a Design, that would be great.

Target Market(s)

Doctors, therapists

Industry/Entity Type

It Professional

Font styles to use
Sans Serif

Requirements
Must have
• Must look uptodate, modern, like new back offices look nowadays

```html
<!DOCTYPE html>
<html lang="de">
<head>
<meta charset="utf-8">
<title>Arzt verwalten</title>
<link href="https://fonts.googleapis.com/css2?family=Open+Sans:wght@400;600;700&display=swap" rel="stylesheet">
<style>
:root{
  --page:#2a2d35;
  --sidebar:#2c2f37;
  --sidebar-line:#383b44;
  --content:#efefef;
  --crumb:#e6e6e6;
  --panel:#ffffff;
  --panel-head:#2f323b;
  --teal:#2dbf9c;
  --blue:#6e9ed6;
  --text:#333333;
  --muted:#555555;
  --border:#d6d6d6;
  --required:#d9302b;
  --footer-band:#e3e3e3;
}
*{box-sizing:border-box;margin:0;padding:0}
html,body{width:1200px;height:829px;overflow:hidden}
body{background:var(--page);font-family:"Open Sans",Arial,sans-serif;color:var(--text);position:relative}
.app-header{position:absolute;left:55px;top:0;width:1090px;height:65px;
  background:linear-gradient(100deg,var(--teal) 0%,#4db4b4 45%,var(--blue) 100%);overflow:hidden}
.app-header .bubble{position:absolute;border-radius:50%;background:rgba(255,255,255,.12)}
.brand{position:absolute;left:32px;top:20px;color:#fff;font-size:20px;font-weight:400}
.user{position:absolute;right:30px;top:20px;display:flex;align-items:center;gap:12px;color:#fff;font-size:15px}
.avatar{width:28px;height:28px;background:#e8e8e8;border:1px solid #fff}
.sidebar{position:absolute;left:55px;top:65px;width:199px;height:731px;background:var(--sidebar)}
.toggle{position:absolute;left:149px;top:18px;width:29px;height:29px;border:2px solid #4a4e58;background:#23262d;border-radius:2px}
.nav{position:absolute;top:66px;left:0;width:199px;list-style:none}
.nav li{height:49px;display:flex;align-items:center;gap:8px;padding-left:6px;color:#fff;font-size:14px;
  border-bottom:2px solid var(--sidebar-line);background:#2f323a;position:relative}
.nav li.active{background:linear-gradient(180deg,var(--teal),var(--blue))}
.nav li.active::after{content:"";position:absolute;right:-8px;top:16px;border:8px solid transparent;border-left-color:var(--blue);border-right:0}
.main{position:absolute;left:254px;top:65px;width:891px;height:731px;background:var(--content)}
.crumb{height:41px;background:var(--crumb);border-bottom:1px solid #d4d4d4;display:flex;align-items:center;gap:6px;padding-left:25px;font-size:13px;color:#222}
.panel{position:absolute;left:29px;top:77px;width:836px;height:604px;background:var(--panel);border:1px solid #d0d0d0}
.panel-head{margin:2px;height:46px;background:var(--panel-head);color:#fff;font-size:15px;padding:14px 18px}
.panel-title{position:absolute;left:26px;top:67px;font-size:19px;font-weight:400;color:#333}
.btn-add{position:absolute;right:15px;top:59px;width:212px;height:34px;background:var(--panel-head);color:#fff;border-radius:3px;
  font-size:13px;font-weight:700;display:flex;align-items:center;justify-content:center;gap:8px;box-shadow:0 2px 3px rgba(0,0,0,.3)}
.divider{position:absolute;left:4px;right:4px;top:108px;border-top:1px solid #e2e2e2}
.form{position:absolute;left:0;top:142px;width:804px;display:grid;grid-template-columns:140px 238px 146px 238px;
  column-gap:14px;row-gap:17.5px;align-items:center}
.form label{text-align:right;font-size:12px;color:var(--muted);white-space:nowrap}
.form label .req{color:var(--required);margin-left:4px}
.field{height:28px;border:1px solid var(--border);font-size:12px;padding:6px 5px;color:#222;border-radius:2px;background:#fff;position:relative;white-space:nowrap;overflow:hidden}
.field.select::after{content:"";position:absolute;right:6px;top:8px;border:3px solid transparent;border-bottom:4px solid #333;border-top:0}
.field.select::before{content:"";position:absolute;right:6px;top:15px;border:3px solid transparent;border-top:4px solid #333;border-bottom:0}
.plain{height:28px}
.status{display:flex;gap:2px;background:#222;width:32px;padding:2px 3px;border-radius:3px}
.status i{width:8px;height:8px;border-radius:50%;background:#777}
.status i.on{background:#2fe04a}
.panel-foot{position:absolute;left:2px;right:2px;bottom:2px;height:89px;background:var(--footer-band)}
.btn{position:absolute;top:32px;width:146px;height:35px;color:#fff;font-weight:700;font-size:14px;border:1px solid #2a9e8a;
  background:linear-gradient(180deg,var(--teal),var(--blue));display:flex;align-items:center;justify-content:center;box-shadow:0 3px 4px rgba(0,0,0,.25)}
.copyright{position:absolute;left:92px;top:805px;font-size:11px;color:#777}
</style>
</head>
<body>
<header class="app-header">
  <span class="bubble" style="left:5px;top:10px;width:16px;height:16px"></span>
  <span class="bubble" style="left:645px;top:20px;width:22px;height:22px"></span>
  <span class="bubble" style="left:710px;top:-30px;width:72px;height:72px"></span>
  <span class="bubble" style="left:878px;top:12px;width:54px;height:54px"></span>
  <span class="bubble" style="left:825px;top:32px;width:14px;height:14px"></span>
  <div class="brand">Header Name (logo)</div>
  <div class="user">
    <svg class="avatar" viewBox="0 0 28 28"><rect width="28" height="28" fill="#e6e6e6"/><circle cx="14" cy="11" r="5" fill="#aaa"/><path d="M4 28c1-7 5-9 10-9s9 2 10 9z" fill="#aaa"/></svg>
    <span>Dr.</span>
    <svg width="12" height="8" viewBox="0 0 12 8" style="margin-left:12px"><path d="M0 1h12L6 7z" fill="#fff"/></svg>
  </div>
</header>

<aside class="sidebar">
  <div class="toggle"><svg width="25" height="25" viewBox="0 0 25 25"><g stroke="#2dbf9c" stroke-width="2"><path d="M6 8h13M6 11h13M6 14h13M6 17h13"/></g></svg></div>
  <ul class="nav">
    <li class="active"><svg width="26" height="20" viewBox="0 0 26 20"><path d="M3 17a10 10 0 1 1 20 0" fill="none" stroke="#fff" stroke-width="3"/><path d="M13 16l5-7" stroke="#fff" stroke-width="3"/></svg>Dashboard</li>
    <li><svg width="26" height="22" viewBox="0 0 26 22"><circle cx="13" cy="5" r="4" fill="#fff"/><path d="M4 21c0-8 4-10 9-10s9 2 9 10z" fill="#fff"/></svg>Main Konto</li>
    <li><svg width="26" height="22" viewBox="0 0 26 22"><path d="M13 2c6 0 11 3.5 11 8s-5 8-11 8c-2 0-3 0-5-1l-5 3 2-5c-2-1.5-3-3-3-5C2 5.5 7 2 13 2z" fill="none" stroke="#fff" stroke-width="2.5"/></svg>Patientenbewertungen</li>
  </ul>
</aside>

<main class="main">
  <nav class="crumb">
    <svg width="16" height="15" viewBox="0 0 16 15"><path d="M8 1L1 8h2v6h4v-4h2v4h4V8h2z" fill="#222"/></svg>
    Start
    <svg width="8" height="10" viewBox="0 0 8 10"><path d="M2 1l4 4-4 4" fill="none" stroke="#222" stroke-width="1.6"/></svg>
  </nav>

  <section class="panel">
    <div class="panel-head">Arzt verwalten</div>
    <h1 class="panel-title">Arzt verwalten</h1>
    <div class="btn-add">Neuen Patient hinzufugen
      <svg width="12" height="12" viewBox="0 0 12 12"><path d="M6 0v12M0 6h12" stroke="#2dbf9c" stroke-width="3"/></svg></div>
    <div class="divider"></div>

    <div class="form">
      <label>Benutzer Rechte<span class="req">*</span></label><div class="field select">Doctor</div>
      <label>Vorname<span class="req">*</span></label><div class="field">Dr.</div>

      <label>Nachname<span class="req">*</span></label><div class="field">Brandauer</div>
      <label>E-Mail<span class="req">*</span></label><div class="field">praxis@mailbeispiel.de</div>

      <label>Tel<span class="req">*</span></label><div class="field">0221 555018200</div>
      <label>Praxisname</label><div class="field">Lindenhof Praxis</div>

      <label>Strasse<span class="req">*</span></label><div class="field">Lindenweg 14</div>
      <label>Postleitzahl</label><div class="field">53111</div>

      <label>Ort<span class="req">*</span></label><div class="field">Bonn</div>
      <label>Deutschland<span class="req">*</span></label><div class="field select">Germany</div>

      <label>Paket<span class="req">*</span></label><div class="field">12 Monate</div>
      <label>Zahlungsart<span class="req">*</span></label><div class="field">MANUAL</div>

      <label>Mitglied seit</label><div class="field">2014-06-03 12:12:05</div>
      <label>Ablauf der Mitgliedschaft</label><div class="field">2015-06-03 12:12</div>

      <label>Website</label><div class="plain"></div>
      <label>Öffentlicher Status</label><div class="plain"><div class="status"><i></i><i></i><i class="on"></i></div></div>
    </div>

    <div class="panel-foot">
      <div class="btn" style="left:475px">Aktualisieren</div>
      <div class="btn" style="left:640px">Storno</div>
    </div>
  </section>
</main>

<footer class="copyright">2014 © Medivo Portal</footer>
</body>
</html>
```